Consulting Company Business Card

I am looking for a minimalist, classy, professional design on my business card. I would like it to be double-sided. I want to use the font and color scheme of my logo which are attached. Please be creative in the designs that you send me. I want to play off the design of my logo with the inner C that is Green and Blue broken up with the white.
Target Market(s)
Small Businesses
Industry/Entity Type
Consulting
Contact Information for Business Card
Dale M. Whitcombe, CPA CGMA, 555-014-2873, dwhitcombe@vorantaadvisory.example, www.vorantaadvisory.example

```html
<!DOCTYPE html>
<html lang="en">
<head>
<meta charset="utf-8">
<title>Voranta Advisory — Business Card</title>
<link rel="stylesheet" href="https://fonts.googleapis.com/css2?family=Poppins:wght@300;400;600&display=swap">
<style>
  :root {
    --navy: #1d2f52;
    --navy-deep: #182a4b;
    --teal: #1f7b7c;
    --paper: #eceef2;
    --backdrop: #e6e7ea;
    --muted: #d4d9e3;
    --blue-soft: #5a7fc0;
  }
  * { margin: 0; padding: 0; box-sizing: border-box; }
  html, body {
    width: 1200px; height: 1200px; overflow: hidden;
    background: var(--backdrop);
    font-family: "Poppins", sans-serif;
  }
  .card {
    position: absolute;
    left: 227px;
    width: 746px; height: 425px;
    border-radius: 56px;
    overflow: hidden;
  }
  .card--front { top: 135px; background: var(--navy); }
  .card--back  { top: 640px; }
  .front-shapes { position: absolute; inset: 0; width: 100%; height: 100%; }

  .brand {
    position: absolute;
    left: 0; width: 332px;
    top: 150px;
    display: flex; flex-direction: column; align-items: center; gap: 14px;
  }
  .brand__dot {
    width: 54px; height: 54px; border-radius: 50%;
    background: var(--navy);
  }
  .brand__name {
    color: var(--navy);
    font-weight: 600;
    font-size: 33px;
    letter-spacing: 1px;
    text-transform: uppercase;
    text-align: center;
    line-height: 1.15;
  }

  .person {
    position: absolute;
    right: 28px; top: 240px;
    text-align: right;
  }
  .person__name {
    color: #f2f4f8;
    font-weight: 600;
    font-size: 23px;
    letter-spacing: 0.5px;
    text-transform: uppercase;
    line-height: 1.1;
  }
  .person__title {
    color: var(--muted);
    font-weight: 300;
    font-size: 18px;
    letter-spacing: 0.5px;
    margin-top: 2px;
  }

  .contact {
    position: absolute;
    right: 27px; top: 320px;
    list-style: none;
  }
  .contact__item {
    display: flex; align-items: center; justify-content: flex-end;
    gap: 12px;
    height: 25px;
    color: #e8ecf3;
    font-weight: 300;
    font-size: 18px;
  }
  .contact__icon {
    width: 18px; height: 18px; flex: none;
  }

  .back-field {
    position: absolute; inset: 0;
    background: linear-gradient(100deg, var(--navy-deep) 0%, var(--navy) 45%, #2c4a84 75%, var(--blue-soft) 100%);
  }
  .back-brand {
    position: absolute;
    left: 520px; top: 285px;
    color: #ffffff;
    font-weight: 600;
    font-size: 22px;
    letter-spacing: 1px;
    text-transform: uppercase;
  }
</style>
</head>
<body>

<section class="card card--front" aria-label="Card front">
  <svg class="front-shapes" viewBox="0 0 746 425" preserveAspectRatio="none" aria-hidden="true">
    <path class="shape-teal" fill="#1f7b7c" d="M0 0 H360 C392 80 410 250 291 425 H0 Z"/>
    <path class="shape-white-stripe" fill="#eceef2" d="M0 0 H358 C384 80 392 250 229 425 H0 Z"/>
    <path class="shape-navy-band" fill="#1d2f52" d="M297 0 H332 C374 110 372 265 245 392 C336 262 346 112 297 0 Z"/>
  </svg>

  <div class="brand">
    <span class="brand__dot"></span>
    <span class="brand__name">Voranta<br>Advisory</span>
  </div>

  <div class="person">
    <p class="person__name">Dale M. Whitcombe</p>
    <p class="person__title">CPA CGMA</p>
  </div>

  <ul class="contact">
    <li class="contact__item">555-014-2873
      <svg class="contact__icon" viewBox="0 0 18 18" aria-hidden="true">
        <circle cx="9" cy="9" r="9" fill="#e8ecf3"/>
        <path d="M5 7.5 C5 5.5 13 5.5 13 7.5 L11.5 8.5 L10.5 7.5 H7.5 L6.5 8.5 Z M6.5 9.5 H11.5 L12.5 12.5 H5.5 Z" fill="#1d2f52"/>
      </svg>
    </li>
    <li class="contact__item">dwhitcombe@vorantaadvisory.example
      <svg class="contact__icon" viewBox="0 0 18 18" aria-hidden="true">
        <circle cx="9" cy="9" r="9" fill="#e8ecf3"/>
        <rect x="4.5" y="5.8" width="9" height="6.4" rx="0.8" fill="none" stroke="#1d2f52" stroke-width="1.2"/>
        <path d="M4.8 6.3 L9 9.6 L13.2 6.3" fill="none" stroke="#1d2f52" stroke-width="1.2"/>
      </svg>
    </li>
    <li class="contact__item">www.vorantaadvisory.example
      <svg class="contact__icon" viewBox="0 0 18 18" aria-hidden="true">
        <circle cx="9" cy="9" r="9" fill="#e8ecf3"/>
        <circle cx="9" cy="9" r="5" fill="none" stroke="#1d2f52" stroke-width="1.2"/>
        <path d="M4 9 H14 M9 4 C6.5 6.5 6.5 11.5 9 14 M9 4 C11.5 6.5 11.5 11.5 9 14" fill="none" stroke="#1d2f52" stroke-width="1"/>
      </svg>
    </li>
  </ul>
</section>

<section class="card card--back" aria-label="Card back">
  <div class="back-field" role="img" aria-label="Embossed repeating brand-mark pattern fading from deep navy to soft blue"></div>
  <p class="back-brand">Voranta Advisory</p>
</section>

</body>
</html>
```